Realm of Ironfall AddOn Banner

We need a static or animated banner for our Realm of Ironfall Mogul AddOn (www.runeglint.example/mogul).

The banner should be 160x600 and should fit zorpa adlinks guidelines.

The text should read:
- GOLD ADDON EARNS 30,000 GOLD PER DAY. 100% LEGAL & WITHOUT CHEATING.
- WANT TO BE FILTHY RICH?
- CLICK HERE NOW

Target Market(s)

18-35 year old gamers

Industry/Entity Type

Legal

Requirements
Must have
• The color scheme should be similar to the following 2 banners:
http://a.tovrimex.example/coin_making_manual/coin_making_manual_160_600.gif

http://a.tovrimex.example/hidden_loot_manual/hidden_loot_manual_728_90.png
Nice to have
• There should probably be some kind of Realm of Ironfall related image. A few keywords you can search zorpa for are:

roi goblin, roi gold coins, roi treasure, roi gnome, roi night elf

```html
<!DOCTYPE html>
<html lang="en">
<head>
<meta charset="utf-8">
<title>Realm of Ironfall Mogul AddOn Banner – Frames</title>
<link rel="stylesheet" href="https://fonts.googleapis.com/css2?family=Cinzel:wght@700;900&family=Arimo:wght@700&display=swap">
<style>
  :root {
    --gap-white: #ffffff;
    --parchment-light: #f6e9db;
    --parchment-mid: #e3d0bd;
    --parchment-dark: #c9b29c;
    --gold-text: #e9b62a;
    --gold-shadow: #5a3a0c;
    --coin-light: #f3c73a;
    --coin-dark: #c98f12;
    --white-text: #ffffff;
    --cta-red: #e60000;
  }
  * { box-sizing: border-box; margin: 0; padding: 0; }
  html, body {
    width: 1200px; height: 634px; overflow: hidden;
    background: var(--gap-white);
  }
  .storyboard {
    width: 1200px; height: 634px;
    display: grid;
    grid-template-columns: repeat(7, 1fr);
    column-gap: 5px;
  }
  .frame {
    position: relative; height: 634px; overflow: hidden;
    background:
      radial-gradient(ellipse 45% 60% at 50% 32%, var(--parchment-light) 0%, rgba(246,233,219,0) 100%),
      linear-gradient(90deg, var(--parchment-dark) 0%, var(--parchment-mid) 25%, var(--parchment-mid) 75%, var(--parchment-dark) 100%);
  }
  .coin-pile {
    position: absolute; left: 0; right: 0; bottom: 0; height: 94px;
    background: linear-gradient(180deg, var(--coin-light) 0%, var(--coin-dark) 100%);
  }
  .line {
    position: absolute; left: 0; right: 0; text-align: center; white-space: nowrap;
  }
  .gold {
    font-family: "Cinzel", "Times New Roman", serif;
    font-weight: 900; font-size: 19px; letter-spacing: 0.2px;
    color: var(--gold-text);
    text-shadow: 0 1px 0 var(--gold-shadow), 1px 0 0 var(--gold-shadow), -1px 0 0 var(--gold-shadow), 0 -1px 0 var(--gold-shadow), 0 2px 4px rgba(0,0,0,.45);
  }
  .gold.compact { font-size: 17px; letter-spacing: 0; }
  .faded { opacity: .3; }
  .plain {
    font-family: "Arimo", Arial, sans-serif; font-weight: 700; font-size: 20px;
    color: var(--white-text); line-height: 27px;
    text-shadow: 0 1px 3px rgba(90,58,12,.55);
  }
  .cta {
    font-family: "Arimo", Arial, sans-serif; font-weight: 700; font-size: 25px;
    color: var(--cta-red); line-height: 41px;
    text-shadow: 0 0 8px #ffffff, 0 0 14px #ffffff;
  }
  .coin {
    position: absolute; width: 24px; height: 20px;
    background: linear-gradient(180deg, var(--coin-light), var(--coin-dark));
  }
</style>
</head>
<body>
<main class="storyboard">
  <section class="frame">
    <p class="line gold faded" style="top:34px">GOLD ADDON</p>
    <div class="coin-pile" role="img" aria-label="Pile of gold coins"></div>
  </section>

  <section class="frame">
    <p class="line gold" style="top:34px">GOLD ADDON</p>
    <p class="line gold" style="top:72px">EARNS</p>
    <p class="line gold faded" style="top:107px">30,000</p>
    <div class="coin-pile" role="img" aria-label="Pile of gold coins"></div>
  </section>

  <section class="frame">
    <p class="line gold" style="top:34px">GOLD ADDON</p>
    <p class="line gold" style="top:72px">EARNS</p>
    <p class="line gold" style="top:107px">30,000</p>
    <p class="line gold compact" style="top:146px">GOLD PER DAY</p>
    <p class="line plain" style="top:192px">100% Legal</p>
    <div class="coin-pile" role="img" aria-label="Pile of gold coins"></div>
  </section>

  <section class="frame">
    <p class="line gold" style="top:34px">GOLD ADDON</p>
    <p class="line gold" style="top:72px">EARNS</p>
    <p class="line gold" style="top:107px">30,000</p>
    <p class="line gold compact" style="top:146px">GOLD PER DAY</p>
    <p class="line plain" style="top:192px">100% Legal</p>
    <p class="line plain" style="top:230px">WITHOUT<br>CHEATING</p>
    <div class="coin-pile" role="img" aria-label="Pile of gold coins"></div>
  </section>

  <section class="frame">
    <p class="line gold" style="top:196px">WANT TO BE</p>
    <p class="line gold" style="top:244px">FILTHY RICH?</p>
    <div class="coin-pile" role="img" aria-label="Pile of gold coins"></div>
  </section>

  <section class="frame">
    <span class="coin" role="img" aria-label="Falling gold coin" style="left:50px;top:0"></span>
    <span class="coin" role="img" aria-label="Falling gold coin" style="left:104px;top:170px"></span>
    <span class="coin" role="img" aria-label="Falling gold coin" style="left:36px;top:322px"></span>
    <span class="coin" role="img" aria-label="Falling gold coin" style="left:80px;top:408px"></span>
    <span class="coin" role="img" aria-label="Falling gold coin" style="left:6px;top:488px"></span>
    <span class="coin" role="img" aria-label="Falling gold coin" style="left:136px;top:493px"></span>
    <div class="coin-pile" role="img" aria-label="Pile of gold coins"></div>
  </section>

  <section class="frame">
    <p class="line cta" style="top:168px">CLICK<br>HERE<br>NOW</p>
    <div class="coin-pile" role="img" aria-label="Pile of gold coins"></div>
  </section>
</main>
</body>
</html>
```